Brackenvale Herons Soccer Club/Duelmark Football Programs needs a flyer for promotions to young students

We are a soccer(football) club based in Melbourne(suburb of Campbellfield) and are running a professional 5 day a week all year round program for kids aged 8 to 18. Our target is to attract approximately 225 kids to our program by the 8th of march this year(4 weeks).
What sets our program apart is our message and mission statement:
- DuelmarkFootball Programs will send players for a European or local Professional trial when they are ready
- Train like a professional 5 days a week all year round
- Proven program over 12 years
- Testimonials on website http://www.brackenvaleherons-qx.com
The message on the flyer needs to be clear and concise.
"Come and try our program FREE for 3 days"
Lorne Habib,Harbourton Rovers 2015/2016 says "..............."
From only $10 a day
Milo Ferrand Reserve cnr Ashgrove and Tulloch Rd Brackenvale
Positions Limited, Register Now.....website..............
Call Rina Obu on 0400918372, Paul Vasko on 0400736154, Peter Stravinou on 0400482690
Example of a flyer uploaded. Can we magnify our message?

Target Market(s)

children and youth aged 8 years to 18 years

Industry/Entity Type

Club

Requirements
Must have
• at least one testimonial
• background image
• clear, concise with no clutter

```html
<!DOCTYPE html>
<html lang="en">
<head>
<meta charset="utf-8">
<title>Brackenvale Herons Soccer Club – Duelmark Football Programs</title>
<link href="https://fonts.googleapis.com/css2?family=Oswald:wght@400;500&family=Roboto:ital,wght@0,300;0,400;0,700;1,300;1,400&family=Roboto+Slab:wght@700&display=swap" rel="stylesheet">
<style>
  :root {
    --navy: #2b2470;
    --green: #8db33a;
    --purple: #5b4fa8;
    --lavender: #c9c4ec;
    --white: #ffffff;
    --stage: #e4e4e4;
  }
  * { margin: 0; padding: 0; box-sizing: border-box; }
  html, body { width: 1005px; height: 1200px; overflow: hidden; background: var(--stage); }
  .flyer {
    position: absolute; left: 78px; top: 0;
    width: 826px; height: 1168px;
    transform: scale(1.0274); transform-origin: top left;
    overflow: hidden; background: var(--navy);
    font-family: "Roboto", Arial, sans-serif; color: var(--white);
  }
  .abs { position: absolute; }
  .hero-photo {
    left: 0; top: 0; width: 826px; height: 470px;
    background: linear-gradient(120deg, #1a1612 0%, #2c241c 38%, #7a6048 58%, #b79a76 74%, #5d6a3a 100%);
  }
  .player-photo {
    left: 503px; top: 550px; width: 323px; height: 618px;
    background: linear-gradient(180deg, #f2f2f2 0%, #e8e9ea 55%, #dfe5d8 100%);
  }
  .shapes { left: 0; top: 0; }
  .club-name {
    left: 25px; top: 34px;
    font-family: "Roboto Slab", Georgia, serif; font-weight: 700;
    font-size: 23px; letter-spacing: 0.5px; color: var(--green); text-transform: uppercase;
  }
  .programme-title { left: 30px; top: 86px; display: flex; align-items: center; gap: 14px; }
  .programme-title .brand {
    font-family: "Oswald", "Arial Narrow", sans-serif; font-weight: 500;
    font-size: 72px; line-height: 1; letter-spacing: -1px;
  }
  .programme-title .kind {
    font-family: "Oswald", "Arial Narrow", sans-serif; font-weight: 400;
    font-size: 38px; line-height: 1.1; text-transform: uppercase;
  }
  .key-facts {
    left: 27px; top: 204px;
    font-family: "Oswald", "Arial Narrow", sans-serif; font-size: 21px; line-height: 36px;
    text-transform: uppercase;
  }
  .price-badge {
    left: 665px; top: 301px; width: 140px; height: 140px; border-radius: 50%;
    background: var(--purple); border: 4px solid var(--white);
    display: flex; flex-direction: column; align-items: center; justify-content: center;
    font-weight: 700; font-size: 17px;
  }
  .price-badge .amount { font-size: 26px; }
  .price-badge .amount small { font-size: 17px; }
  .trial-offer {
    right: 23px; top: 472px; text-align: right;
    font-family: "Oswald", "Arial Narrow", sans-serif; font-size: 28px; line-height: 37px;
    text-transform: uppercase;
  }
  .headline {
    left: 24px; top: 520px;
    font-family: "Oswald", "Arial Narrow", sans-serif; font-weight: 500;
    font-size: 34px; line-height: 48px; text-transform: uppercase;
  }
  .headline .proven { color: var(--green); margin-top: 10px; display: block; }
  .mission { left: 24px; top: 694px; width: 470px; font-weight: 300; font-size: 25px; line-height: 31px; }
  .venue { left: 24px; top: 816px; font-weight: 300; font-size: 25px; line-height: 31px; }
  .testimonials { left: 24px; top: 904px; width: 480px; list-style: none; }
  .testimonials li { position: relative; padding-left: 34px; height: 59px; }
  .testimonials li::before {
    content: "\201C"; position: absolute; left: 0; top: -12px;
    font-family: Georgia, serif; font-size: 44px; color: var(--purple);
  }
  .testimonials .quote { font-style: italic; font-size: 18px; color: var(--lavender); }
  .testimonials .source { font-style: italic; font-size: 15px; color: var(--lavender); margin-top: 2px; }
  .register-bar {
    left: 0; top: 1078px; width: 523px; height: 90px; background: var(--green);
    text-align: center; padding-top: 8px;
  }
  .register-bar .cta { font-family: "Oswald", "Arial Narrow", sans-serif; font-weight: 500; font-size: 33px; line-height: 40px; }
  .register-bar .url { font-weight: 700; font-size: 21px; }
  .contacts { right: 13px; top: 1078px; list-style: none; text-align: right; }
  .contacts li { font-weight: 700; font-size: 17px; line-height: 25.5px; color: var(--navy); }
  .contacts .phone { color: var(--purple); }
  .contacts svg { vertical-align: -1px; margin: 0 2px 0 4px; }
</style>
</head>
<body>
<main class="flyer">
  <div class="abs hero-photo" role="img" aria-label="Stadium action photo of a young player striking a football under floodlights"></div>
  <div class="abs player-photo" role="img" aria-label="Studio photo of a smiling young player in kit with one foot on a ball"></div>

  <svg class="abs shapes" width="826" height="1168" viewBox="0 0 826 1168" aria-hidden="true">
    <polygon points="0,0 565,0 0,395" fill="#000" opacity="0.55"/>
    <polygon points="0,308 133,388 0,507" fill="var(--green)"/>
    <polygon points="0,507 133,388 503,550 503,1168 0,1168" fill="var(--navy)"/>
    <polygon points="309,465 826,465 826,550 503,550" fill="var(--green)"/>
  </svg>

  <p class="abs club-name">Brackenvale Herons Soccer Club</p>
  <h1 class="abs programme-title">
    <span class="brand">DUELMARK</span>
    <span class="kind">Football<br>Programs</span>
  </h1>
  <p class="abs key-facts">Register by the 8th of March<br>Kids aged 8 to 18</p>

  <div class="abs price-badge"><span>From only</span><span class="amount">$10 <small>a day</small></span></div>

  <p class="abs trial-offer">Come and try our program<br>Free for 3 days</p>

  <h2 class="abs headline">Train like a professional<br>5 days a week all year round<span class="proven">Proven program over 12 years</span></h2>

  <p class="abs mission">DuelmarkFootball Programs will send players for a European or local Professional trial when they are ready.</p>
  <p class="abs venue">Milo Ferrand Reserve cnr Ashgrove<br>and Tulloch Rd Brackenvale.</p>

  <ul class="abs testimonials">
    <li><p class="quote">Wouldn’t be here without you”</p><p class="source">Lorne Habib - Coast League Harbourton Rovers Seniors 2015</p></li>
    <li><p class="quote">Your duel training brought me here”</p><p class="source">Dario Kesh Coast League Harbourton Rovers</p></li>
    <li><p class="quote">You showed more than I knew”</p><p class="source">Tomas Verelli, Coast League Harbourton Rovers - youth - 2011/13</p></li>
  </ul>

  <div class="abs register-bar">
    <p class="cta">REGISTER NOW</p>
    <p class="url">www.brackenvaleherons-qx.com</p>
  </div>

  <ul class="abs contacts">
    <li>Rina Obu<svg width="13" height="13" viewBox="0 0 24 24"><path fill="var(--purple)" d="M6.6 10.8a15.1 15.1 0 0 0 6.6 6.6l2.2-2.2a1 1 0 0 1 1-.25 11.4 11.4 0 0 0 3.6.57 1 1 0 0 1 1 1V20a1 1 0 0 1-1 1A17 17 0 0 1 3 4a1 1 0 0 1 1-1h3.5a1 1 0 0 1 1 1c0 1.25.2 2.45.57 3.57a1 1 0 0 1-.25 1z"/></svg><span class="phone">0400918372</span></li>
    <li>Paul Vasko<svg width="13" height="13" viewBox="0 0 24 24"><path fill="var(--purple)" d="M6.6 10.8a15.1 15.1 0 0 0 6.6 6.6l2.2-2.2a1 1 0 0 1 1-.25 11.4 11.4 0 0 0 3.6.57 1 1 0 0 1 1 1V20a1 1 0 0 1-1 1A17 17 0 0 1 3 4a1 1 0 0 1 1-1h3.5a1 1 0 0 1 1 1c0 1.25.2 2.45.57 3.57a1 1 0 0 1-.25 1z"/></svg><span class="phone">0400736154</span></li>
    <li>Peter Stravinou<svg width="13" height="13" viewBox="0 0 24 24"><path fill="var(--purple)" d="M6.6 10.8a15.1 15.1 0 0 0 6.6 6.6l2.2-2.2a1 1 0 0 1 1-.25 11.4 11.4 0 0 0 3.6.57 1 1 0 0 1 1 1V20a1 1 0 0 1-1 1A17 17 0 0 1 3 4a1 1 0 0 1 1-1h3.5a1 1 0 0 1 1 1c0 1.25.2 2.45.57 3.57a1 1 0 0 1-.25 1z"/></svg><span class="phone">0400482690</span></li>
  </ul>
</main>
</body>
</html>
```